Real Estate Brokerage - Sales Promo Flyer

We would like someone to design a 8x11 high gloss promotional flyer for our real estate agents to use in the field when presenting to a possible listing client (someone who wants to sell their home).

The flyer should include some of our brokerage's recent sales transaction numbers, as well as benefits to using our service.

We would like our design to have a professional appeal, with bold colors, and vivid images.

I have attached 5 images of recently sold homes:
248 Marlowe Bend Trust, Palm Beach Gardens, Florida - Sold for $424,000
4172 Fenwick Hollow Ct, Boca Raton, FL 33498 - Sold for $415,000
276 Ravelston Drive, Palm Beach Gardens, Florida - Sold for $877,500
24817 Thistle Loop, West Palm Beach, Florida - Sold for $380,000
358 Pellam Road, Greenacres, Florida - Sold for $234,500

I can provide any additional details you need. See attached files.
Updates

This flyer should contain our business name, logo, phone numbers, and website (however you see fit). BrellowHomes Palm Beach County | (561) 240-3186 Broward County | (954) 372-8415 www.brellowhomes-example.com

More Properties to Add: 276 Ravelston Drive, Palm Beach Gardens, Florida - Sold for $877,500 24817 Thistle Loop, West Palm Beach, Florida - Sold for $380,000 358 Pellam Road, Greenacres, Florida - Sold for $234,500

I have added the Original Logo Images. Please use one of these in your design.

I have uploaded an image of our syndication partners, please add this to your flyers.

Please submit all of your Design. Thanks!

Please submit your edits

Industry/Entity Type

Real Estate

Requirements
Must have
• BrellowHomes is one word with a capital K and capital R.

Must have website and phone number.

BrellowHomes
www.brellowhomes-example.com
561-240-3186 - Palm Beach County
954-372-8415 - Broward County

```html
<!DOCTYPE html>
<html lang="en">
<head>
<meta charset="utf-8">
<title>BrellowHomes – Recent Sales Flyer</title>
<link rel="stylesheet" href="https://fonts.googleapis.com/css2?family=Open+Sans:ital,wght@0,400;0,600;0,700;1,400&family=Oswald:wght@500;600&display=swap">
<style>
  :root {
    --paper: #efefef;
    --ink: #555a5e;
    --ink-soft: #7a7f83;
    --teal: #3fb6d8;
    --teal-bright: #1ab0d6;
    --teal-deep: #1990b2;
    --bar: #6b6d70;
    --photo-sky: #cfe3ef;
    --photo-wall: #d8c9a0;
    --photo-green: #6f8f4c;
  }
  * { box-sizing: border-box; margin: 0; padding: 0; }
  html, body { width: 933px; height: 1200px; overflow: hidden; background: var(--paper); }
  body { font-family: "Open Sans", Arial, sans-serif; color: var(--ink); }

  .flyer { position: relative; width: 933px; height: 1200px; background: var(--paper); }

  .brand { height: 110px; display: flex; align-items: center; justify-content: center; gap: 12px; }
  .brand-mark { width: 30px; height: 30px; border-radius: 50%; background: var(--teal-deep); }
  .brand-name { font-size: 26px; font-weight: 600; color: var(--ink); letter-spacing: 1px; }

  .accent-stripe { height: 14px; background: var(--teal); }

  .hero-photo {
    position: absolute; top: 124px; left: 0; width: 933px; height: 533px;
    background: linear-gradient(180deg, var(--photo-sky) 0%, #e6e8e0 30%, var(--photo-wall) 55%, var(--photo-green) 82%, #9a8a72 100%);
  }
  .hero-curve { position: absolute; top: 560px; left: 0; width: 933px; height: 100px; }

  .feature-banner {
    position: absolute; top: 594px; left: 152px; width: 627px; height: 111px;
    display: flex; box-shadow: 0 4px 8px rgba(0,0,0,.18);
  }
  .feature-address { flex: 0 0 389px; background: var(--teal-bright); color: #fff; padding: 18px 0 0 26px; }
  .feature-address h1 { font-size: 31px; font-weight: 700; line-height: 1.15; white-space: nowrap; }
  .feature-address p { font-size: 20px; line-height: 1.3; }
  .feature-price { flex: 1; background: var(--teal-deep); color: #fff; text-align: center; padding-top: 12px; }
  .feature-price .label { font-size: 26px; font-weight: 600; display: block; }
  .feature-price .amount { font-size: 41px; font-weight: 400; line-height: 1.15; }

  .section-title {
    position: absolute; top: 724px; left: 0; width: 933px;
    display: flex; align-items: center; justify-content: center; gap: 16px;
    font-size: 24px; font-style: italic; color: var(--ink-soft);
  }
  .section-title::before, .section-title::after { content: ""; width: 100px; height: 1px; background: #9a9da0; }

  .recent-sales { position: absolute; top: 784px; left: 40px; width: 853px; display: flex; justify-content: space-between; }
  .sale { width: 194px; text-align: center; }
  .sale-photo { height: 124px; border: 4px solid #fff; box-shadow: 0 6px 8px rgba(0,0,0,.25); }
  .sale-photo.one { background: linear-gradient(180deg, #b9d6ea 0%, #d7d3c0 50%, #6f9a4e 100%); }
  .sale-photo.two { background: linear-gradient(180deg, #cde0ea 0%, #b8b09a 48%, #5f8a3e 100%); }
  .sale-photo.three { background: linear-gradient(180deg, #c3d8e6 0%, #c9c2b0 45%, #6f7f5a 100%); }
  .sale-photo.four { background: linear-gradient(180deg, #c7dbe7 0%, #6f9250 55%, #8fa36a 100%); }
  .sale h2 { margin-top: 18px; font-family: "Oswald", Arial, sans-serif; font-weight: 500; font-size: 17px; color: var(--ink); text-transform: uppercase; letter-spacing: .2px; white-space: nowrap; }
  .sale p { font-size: 13px; color: var(--ink-soft); line-height: 1.3; white-space: nowrap; }
  .sale-status { margin-top: 6px; display: inline-flex; align-items: center; gap: 8px; }
  .sale-status span { background: var(--teal-bright); color: #fff; font-size: 11px; font-style: italic; padding: 2px 14px; white-space: nowrap; }
  .sale-status svg { width: 14px; height: 14px; }

  .call-to-action { position: absolute; top: 1012px; left: 0; width: 933px; text-align: center; font-family: "Oswald", Arial, sans-serif; font-weight: 600; font-size: 44px; line-height: 1.3; color: var(--ink); letter-spacing: .5px; }
  .contact-line { position: absolute; top: 1082px; left: 0; width: 933px; text-align: center; font-size: 17px; line-height: 24px; color: var(--ink-soft); white-space: nowrap; }

  .partners { position: absolute; top: 1124px; left: 0; width: 933px; display: flex; justify-content: center; align-items: center; gap: 12px; }
  .partner { height: 20px; border-radius: 3px; background: #b9bcbf; }
  .partner.square { width: 22px; height: 22px; border-radius: 0; background: #444; }

  .footer-bar { position: absolute; bottom: 0; left: 0; width: 933px; height: 44px; background: var(--bar); }
</style>
</head>
<body>
<main class="flyer">
  <header class="brand">
    <span class="brand-mark"></span>
    <span class="brand-name">BrellowHomes</span>
  </header>
  <div class="accent-stripe"></div>

  <div class="hero-photo" role="img" aria-label="Photo of a two-storey Mediterranean-style home with tiled roof, tall palm trees and a paver driveway"></div>
  <svg class="hero-curve" viewBox="0 0 933 100" preserveAspectRatio="none" aria-hidden="true">
    <path d="M0,10 Q466,110 933,10 L933,100 L0,100 Z" fill="#efefef"/>
    <path d="M0,26 Q180,70 330,84" fill="none" stroke="#3fb6d8" stroke-width="8"/>
    <path d="M933,26 Q753,70 603,84" fill="none" stroke="#3fb6d8" stroke-width="8"/>
  </svg>

  <section class="feature-banner">
    <div class="feature-address">
      <h1>276 Ravelston Drive,</h1>
      <p>Palm Beach Gardens, Florida</p>
    </div>
    <div class="feature-price">
      <span class="label">Sold for</span>
      <span class="amount">$877,500</span>
    </div>
  </section>

  <div class="section-title">Other Recent Sales</div>

  <section class="recent-sales">
    <article class="sale">
      <div class="sale-photo one" role="img" aria-label="Photo of a single-storey home with palm trees and lawn"></div>
      <h2>248 Marlowe Bend Trust,</h2>
      <p>Palm Beach Gardens, Florida</p>
      <div class="sale-status"><span>Sold for $424,000</span><svg viewBox="0 0 14 14"><path d="M2,7 L6,11 L12,3" fill="none" stroke="#1ab0d6" stroke-width="2"/></svg></div>
    </article>
    <article class="sale">
      <div class="sale-photo two" role="img" aria-label="Photo of a ranch-style home with a wide green lawn and driveway"></div>
      <h2>24817 Thistle Loop</h2>
      <p>West Palm Beach, Florida</p>
      <div class="sale-status"><span>Sold for $380,000</span><svg viewBox="0 0 14 14"><path d="M2,7 L6,11 L12,3" fill="none" stroke="#1ab0d6" stroke-width="2"/></svg></div>
    </article>
    <article class="sale">
      <div class="sale-photo three" role="img" aria-label="Photo of a home with a garage and landscaped front yard"></div>
      <h2>358 Pellam Road</h2>
      <p>Greenacres, Florida</p>
      <div class="sale-status"><span>Sold for $234,500</span><svg viewBox="0 0 14 14"><path d="M2,7 L6,11 L12,3" fill="none" stroke="#1ab0d6" stroke-width="2"/></svg></div>
    </article>
    <article class="sale">
      <div class="sale-photo four" role="img" aria-label="Photo of a home behind a large shade tree and lawn"></div>
      <h2>4172 Fenwick Hollow Ct</h2>
      <p>Boca Raton, Florida</p>
      <div class="sale-status"><span>Sold for $415,000</span><svg viewBox="0 0 14 14"><path d="M2,7 L6,11 L12,3" fill="none" stroke="#1ab0d6" stroke-width="2"/></svg></div>
    </article>
  </section>

  <div class="call-to-action">CALL US NOW:</div>
  <p class="contact-line">(561) 240-3186 | Palm Beach County &nbsp;(954) 372-8415 | Broward County &nbsp;www.brellowhomes-example.com</p>

  <div class="partners" aria-label="Syndication partners">
    <span class="partner" style="width:104px"></span>
    <span class="partner" style="width:72px"></span>
    <span class="partner" style="width:96px"></span>
    <span class="partner" style="width:66px"></span>
    <span class="partner" style="width:112px"></span>
    <span class="partner square"></span>
    <span class="partner square"></span>
  </div>

  <div class="footer-bar"></div>
</main>
</body>
</html>
```